HTML Digital Sign layout and code (one page)...save us from the 60's!

Digital Sign for Headquarters Entrance

HTML Digital Sign layout (one page)...save us from the 60's!

Good Day Designers!

We have decided to install Digital Signage in our headquarters building that will replace the “felt boards” that the administrative staff use at our building entrances.

Instead of the information being displayed on the archaic sign boards, it will be presented on a landscaped 50inch LCD screen running at 1920x1080

We are looking for a one page HTML design that encompass the following elements:

+ Our Logo
+ Our Company Name (Vorlan Aerotek)
+ Our "Tag Line" - "Progress Shaped By Practice, Quality Shaped By Dedication"
+ Date and Time
+ A space for Today’s Birthdays (which could be up to 4 people)
+ A space for Today’s Anniversaries (which could be up to 4 people)
+ A space for Today’s Visitor (which could be up to 2 people)
+ A space for a Picture of the Day
+ A space for Weather Forecast (perhaps a graphic)
+ A small "banner" section or strip for scrolling Notices / Alerts (perhaps at the bottom of the page?)

The deliverables for the layout need to include the HTML, applicable CSS, HTML code, etc. We need this to be relatively turnkey.

I have included in the contest package a hi-res JPG and AI for our Company Logo.

From a color pallet perspective:

Light Blue:
RGB - 21, 191,242
HEX - #15BFF2

Dark Blue:
RGB - 0, 70, 154
HEX - #00469A

Additionally, I have done a contest like this before (for another company I was at) and have included a screen shot of that final display.

PLEASE NOTE: IT DOES NOT HAVE TO LOOK EXACTLY LIKE THE ATTACHED SCREEN SHOT FROM THE PREVIOUS CONTEST. Including the screenshot was just to give you a general idea of some inspiration and objectives.

Feedback and questions are encouraged.

Target Market(s)

Our Employees

Industry/Entity Type

Digital

Number of Pages Required

1 page

Requirements
Must have
• + Our Logo
• + Our Company Name (Vorlan Aerotek)
• + Our "Tag Line" - "Progress Shaped By Practice, Quality Shaped By Dedication"
• + Date and Time
• + A space for Today’s Birthdays (which could be up to 4 people)
• + A space for Today’s Anniversaries (which could be up to 4 people)
• + A space for Today’s Visitor (which could be up to 2 people)
• + A space for a Picture of the Day
• + A space for Weather Forecast (perhaps a graphic)
• + A small "banner" section or strip for scrolling Notices / Alerts (perhaps at the bottom of the page?)

```html
<!DOCTYPE html>
<html lang="en">
<head>
<meta charset="utf-8">
<title>Vorlan Aerotek – Entrance Display</title>
<link rel="stylesheet" href="https://fonts.googleapis.com/css2?family=Arimo:wght@400;700&display=swap">
<style>
  :root {
    --navy: #1c3585;
    --brand-dark: #1c3f8f;
    --bar-top: #2c62b4;
    --bar-bottom: #0f3d8e;
    --tagline: #0a7cc4;
    --alert-main: #0a7cc4;
    --alert-label: #0a5ea8;
    --sky-top: #0e5aa6;
    --sky-mid: #3a9ad8;
    --sky-light: #bfe3f6;
    --text-muted: #555b63;
    --panel-edge: #d6d9dd;
    --white: #ffffff;
  }
  * { box-sizing: border-box; margin: 0; padding: 0; }
  html, body { width: 1200px; height: 675px; overflow: hidden; }
  body {
    position: relative;
    font-family: "Arimo", Arial, sans-serif;
    background: var(--white);
  }

  .masthead {
    position: absolute; left: 0; top: 0; width: 1200px; height: 186px;
    background: linear-gradient(180deg, #ffffff 0%, #ffffff 70%, #eef0f2 100%);
  }
  .brand-name {
    position: absolute; left: 45px; top: 34px;
    font-weight: 700; font-size: 46px; line-height: 52px;
    color: var(--brand-dark); letter-spacing: 0.5px;
  }
  .masthead-divider {
    position: absolute; left: 365px; top: 25px; width: 1px; height: 132px;
    background: #d9dde2;
  }
  .tagline {
    position: absolute; left: 385px; top: 79px;
    font-weight: 700; font-size: 27.5px; line-height: 32px;
    color: var(--tagline); white-space: nowrap;
  }
  .date-time {
    position: absolute; left: 385px; top: 124px;
    font-weight: 700; font-size: 16px; line-height: 20px;
    color: var(--brand-dark); white-space: nowrap;
  }
  .date-time .clock { color: var(--tagline); margin-left: 10px; }

  .backdrop {
    position: absolute; left: 0; top: 186px; width: 1200px; height: 443px;
    background: linear-gradient(180deg, var(--sky-top) 0%, var(--sky-mid) 30%, #7cc2ea 52%, var(--sky-light) 64%, #ffffff 78%, #ffffff 100%);
  }

  .panel {
    position: absolute;
    border-radius: 3px;
    background: linear-gradient(180deg, #ffffff 0%, #ffffff 62%, #eceef0 100%);
    box-shadow: 0 1px 2px rgba(0,0,0,0.25);
    border: 1px solid var(--panel-edge);
    overflow: hidden;
  }
  .panel-bar {
    height: 50px;
    background: linear-gradient(180deg, var(--bar-top) 0%, var(--bar-bottom) 100%);
    display: flex; align-items: center; justify-content: space-between;
    padding: 0 16px 0 14px;
  }
  .panel-title {
    color: var(--white); font-weight: 700; font-size: 27px; letter-spacing: -0.3px;
  }
  .panel-icon { width: 32px; height: 32px; }
  .name-list { list-style: none; padding: 5px 0 0 19px; }
  .name-list li {
    font-size: 12.5px; line-height: 29px; color: var(--text-muted);
  }

  .picture-panel { left: 12px; top: 202px; width: 353px; height: 394px; }
  .picture-frame {
    margin: 17px 0 0 17px; width: 317px; height: 193px;
    background: linear-gradient(120deg, #1f4a78 0%, #4f8fbf 40%, #9fc6de 70%, #d8e4ec 100%);
  }
  .picture-caption {
    margin: 12px 0 0 17px;
    font-weight: 700; font-size: 15px; color: var(--brand-dark);
  }
  .picture-text {
    margin: 5px 17px 0 17px;
    font-size: 12px; line-height: 18px; color: var(--text-muted);
  }

  .birthdays-panel { left: 377px; top: 202px; width: 383px; height: 147px; }
  .anniversaries-panel { left: 774px; top: 202px; width: 383px; height: 147px; }
  .visitors-panel { left: 377px; top: 360px; width: 383px; height: 157px; }
  .visitors-panel .name-list { padding-top: 6px; }
  .weather-panel { left: 774px; top: 360px; width: 383px; height: 157px; }
  .weather-placeholder {
    padding: 40px 0 0 19px; font-size: 12.5px; color: var(--text-muted);
  }

  .alerts-strip {
    position: absolute; left: 377px; top: 528px; width: 781px; height: 69px;
    border-radius: 3px; overflow: hidden;
    background: var(--alert-main);
    display: flex; align-items: center;
  }
  .alerts-label {
    width: 111px; height: 100%;
    background: var(--alert-label);
    display: flex; align-items: center; justify-content: center;
    color: var(--white); font-weight: 700; font-size: 27px;
  }
  .alerts-message {
    padding-left: 16px; color: var(--white); font-size: 12.5px; white-space: nowrap;
  }

  .site-footer {
    position: absolute; left: 0; top: 629px; width: 1200px; height: 46px;
    background: var(--navy);
    display: flex; align-items: center; justify-content: center;
    color: var(--white); font-weight: 700; font-size: 18px;
  }
</style>
</head>
<body>
  <header class="masthead">
    <div class="brand-name">Vorlan<br>Aerotek</div>
    <div class="masthead-divider"></div>
    <p class="tagline">Progress Shaped By Practice, Quality Shaped By Dedication</p>
    <p class="date-time"><time datetime="2014-03-10">Monday, March 10, 2014</time><time class="clock" datetime="09:30">9:30 AM</time></p>
  </header>

  <div class="backdrop"></div>

  <section class="panel picture-panel">
    <div class="panel-bar">
      <h2 class="panel-title">Picture of the day</h2>
      <svg class="panel-icon" viewBox="0 0 32 32" fill="none" stroke="#fff" stroke-width="1.6">
        <rect x="3" y="5" width="26" height="24" rx="2"/>
        <line x1="3" y1="11" x2="29" y2="11"/>
        <line x1="9" y1="2" x2="9" y2="7"/><line x1="23" y1="2" x2="23" y2="7"/>
        <g fill="#fff" stroke="none">
          <rect x="7" y="14" width="3" height="3"/><rect x="12" y="14" width="3" height="3"/><rect x="17" y="14" width="3" height="3"/><rect x="22" y="14" width="3" height="3"/>
          <rect x="7" y="19" width="3" height="3"/><rect x="12" y="19" width="3" height="3"/><rect x="17" y="19" width="3" height="3"/><rect x="22" y="19" width="3" height="3"/>
          <rect x="7" y="24" width="3" height="2"/><rect x="12" y="24" width="3" height="2"/>
        </g>
      </svg>
    </div>
    <div class="picture-frame" role="img" aria-label="Picture of the day: a hand touching a tablet with a glowing network overlay"></div>
    <h3 class="picture-caption">Image brief description</h3>
    <p class="picture-text">Lorem ipsum dolor sit amet lorem ipsum dolor sit lorsit amet lorem ipsum dolor sit lorem ipsum lorem ips dolor sum dolor sit amet lorem ipsum.<br>Lorem Ipsum is simply dummy text of the printing and typesetting industry.</p>
  </section>

  <section class="panel birthdays-panel">
    <div class="panel-bar">
      <h2 class="panel-title">Today’s Birthdays</h2>
      <svg class="panel-icon" viewBox="0 0 32 32" fill="#fff">
        <path d="M16 3c1.5 2 2 3 0 5-2-2-1.5-3 0-5z"/>
        <rect x="15" y="9" width="2" height="5"/>
        <path d="M7 15h18v5c-1.5 1-3 1-4.5 0-1.5 1-3 1-4.5 0-1.5 1-3 1-4.5 0-1.5 1-3 1-4.5 0z"/>
        <rect x="7" y="21.5" width="18" height="5"/>
        <rect x="3" y="27.5" width="26" height="2"/>
      </svg>
    </div>
    <ul class="name-list">
      <li>First Name, Last Name one</li>
      <li>First Name, Last Name two</li>
      <li>First Name, Last Name three</li>
    </ul>
  </section>

  <section class="panel anniversaries-panel">
    <div class="panel-bar">
      <h2 class="panel-title">Today’s Anniversaries</h2>
      <svg class="panel-icon" viewBox="0 0 32 32" fill="none" stroke="#fff" stroke-width="2.2">
        <circle cx="11.5" cy="18" r="8.5"/>
        <circle cx="20.5" cy="18" r="8.5"/>
        <path d="M9 7l2.5-3 2.5 3M18 7l2.5-3 2.5 3" stroke-width="1.6"/>
      </svg>
    </div>
    <ul class="name-list">
      <li>First Name, Last Name one</li>
      <li>First Name, Last Name two</li>
      <li>First Name, Last Name three</li>
    </ul>
  </section>

  <section class="panel visitors-panel">
    <div class="panel-bar">
      <h2 class="panel-title">Today’s Visitors</h2>
      <svg class="panel-icon" viewBox="0 0 36 32" fill="none" stroke="#fff" stroke-width="1.6">
        <rect x="2" y="8" width="32" height="21" rx="2"/>
        <rect x="15" y="2" width="6" height="9" rx="1.5"/>
        <circle cx="11" cy="17" r="3"/>
        <path d="M6 25c0-3 2.5-4.5 5-4.5s5 1.5 5 4.5"/>
        <line x1="20" y1="16" x2="30" y2="16"/><line x1="20" y1="20" x2="30" y2="20"/><line x1="20" y1="24" x2="27" y2="24"/>
      </svg>
    </div>
    <ul class="name-list">
      <li>First Name, Last Name one</li>
      <li>First Name, Last Name two</li>
      <li>First Name, Last Name three</li>
    </ul>
  </section>

  <section class="panel weather-panel">
    <div class="panel-bar">
      <h2 class="panel-title">Weather Forecast</h2>
      <svg class="panel-icon" viewBox="0 0 36 32" fill="none" stroke="#fff" stroke-width="1.8">
        <circle cx="13" cy="12" r="5"/>
        <path d="M13 2v3M13 19v2M3 12h3M5.5 4.5l2 2M20.5 4.5l-2 2M5.5 19.5l2-2"/>
        <path d="M12 28h18a5 5 0 0 0 0-10 7 7 0 0 0-13-1 5.5 5.5 0 0 0-5 11z" fill="var(--bar-bottom)"/>
      </svg>
    </div>
    <p class="weather-placeholder">(Weather Forecast Graphic Here)</p>
  </section>

  <section class="alerts-strip">
    <h2 class="alerts-label">Alerts</h2>
    <p class="alerts-message">Lorem Ipsum is simply dummy text of the printing and typesetting industry. Lorem Ipsum has been the industry’s</p>
  </section>

  <footer class="site-footer">Copyright © 2014 Vorlan Aerotek. All Rights Reserved.</footer>
</body>
</html>
```